Corporate Design für Steuerberatung
Zielgruppe
Wir sind eine junge Steuerkanzlei und möchten mit hochwertigem, modernem und zeitlosem Design überzeugen. Der Mandantenstamm ist vielfältig, und erstreckt sich über ein Alter von 20 Jahre bis hin zu 75 Jahre.
Aufgabenstellung
Das Design soll möglichst schnörkellos sein, modern aber gleichzeitig auch klassisch und zeitlos. Eher exklusiv und 'maskulin' gehalten.
Die Buchstaben tbr können klein oder in Großbuchstaben geschrieben werden, auch mit Strichen, Punkten oder anderen Formen von einander getrennt sein.

```html
<!DOCTYPE html>
<html lang="de">
<head>
<meta charset="utf-8">
<title>TBR Steuerberatung – Corporate Design</title>
<link rel="stylesheet" href="https://fonts.googleapis.com/css2?family=Questrial&display=swap">
<style>
  :root {
    --brand-blue: #536cb0;
    --text-grey: #6b6b6b;
    --paper: #ffffff;
    --top-bg: #f8f8f8;
    --stage-bg: #ececec;
    --desk-grey: #b3b3b3;
    --sans: "Questrial", "Helvetica Neue", Arial, sans-serif;
  }
  * { margin: 0; padding: 0; box-sizing: border-box; }
  html, body { width: 1200px; height: 2644px; overflow: hidden; }
  body { font-family: var(--sans); color: var(--text-grey); background: var(--top-bg); position: relative; }

  .wordmark { color: var(--brand-blue); font-family: var(--sans); font-weight: 400; text-align: center; line-height: 1; }
  .wordmark__name { display: block; letter-spacing: 0.06em; }
  .wordmark__line { display: block; letter-spacing: 0.42em; color: var(--text-grey); }
  .card .wordmark__line { color: var(--brand-blue); }
  .wordmark--white, .wordmark--white .wordmark__line { color: var(--paper); }

  .brand-section { position: absolute; left: 0; top: 0; width: 1200px; height: 505px; background: var(--top-bg); }
  .brand-section .wordmark { position: absolute; left: 0; top: 145px; width: 1200px; }
  .brand-section .wordmark__name { font-size: 140px; }
  .brand-section .wordmark__line { font-size: 19px; margin-top: 30px; padding-left: 0.42em; }

  .card-section { position: absolute; left: 0; top: 505px; width: 1200px; height: 775px; background: var(--stage-bg); }
  .card { position: absolute; width: 330px; height: 530px; box-shadow: 0 10px 24px rgba(0,0,0,.18); }
  .card--front { left: 200px; top: 125px; background: var(--paper); padding: 60px 36px; }
  .card--back { left: 670px; top: 125px; background: var(--brand-blue); display: flex; align-items: center; justify-content: center; }
  .card .wordmark__name { font-size: 60px; }
  .card .wordmark__line { font-size: 10px; margin-top: 12px; padding-left: 0.42em; }
  .card__person { margin-top: 46px; text-align: right; font-size: 11px; letter-spacing: 0.08em; font-variant: small-caps; line-height: 1.6; }
  .card__name { color: var(--brand-blue); font-size: 14px; }
  .card__contact { margin-top: 70px; font-size: 11px; letter-spacing: 0.08em; font-variant: small-caps; line-height: 1.75; }
  .card__contact .gap { height: 12px; }

  .letter-section { position: absolute; left: 0; top: 1280px; width: 1200px; height: 1364px; background: var(--desk-grey); }
  .letterhead { position: absolute; left: 200px; top: 120px; width: 800px; height: 1132px; background: var(--paper); box-shadow: 0 12px 40px rgba(0,0,0,.35); }
  .letterhead .wordmark { position: absolute; left: 0; top: 52px; width: 800px; }
  .letterhead .wordmark__name { font-size: 68px; }
  .letterhead .wordmark__line { font-size: 12px; margin-top: 14px; padding-left: 0.42em; }
  .letterhead__sender { position: absolute; left: 61px; top: 212px; font-size: 6px; letter-spacing: 0.08em; font-variant: small-caps; }
  .fold-mark { position: absolute; left: 8px; width: 12px; height: 1px; background: var(--text-grey); }
  .fold-mark--upper { top: 397px; }
  .fold-mark--lower { top: 797px; }
  .letterhead__footer { position: absolute; left: 64px; right: 26px; top: 1063px; display: flex; justify-content: space-between; font-size: 8px; letter-spacing: 0.1em; font-variant: small-caps; line-height: 1.55; text-align: right; }
  .letterhead__footer .accent { color: var(--brand-blue); }
</style>
</head>
<body>

<section class="brand-section">
  <div class="wordmark">
    <span class="wordmark__name">TBR</span>
    <span class="wordmark__line">STEUERBERATUNG</span>
  </div>
</section>

<section class="card-section">
  <article class="card card--front">
    <div class="wordmark">
      <span class="wordmark__name">TBR</span>
      <span class="wordmark__line">STEUERBERATUNG</span>
    </div>
    <div class="card__person">
      <div class="card__name">Jonas Feldmann</div>
      <div>Steuerberater</div>
      <div>Wirtschaftsprüfer</div>
    </div>
    <div class="card__contact">
      <div>TBR Steuerberater GmbH</div>
      <div>Lindenweg 17</div>
      <div>72614 Grünhain</div>
      <div class="gap"></div>
      <div>Telefon: +49 (0) 7341 208 514</div>
      <div>Telefax: +49 (0) 7341 208 515</div>
      <div class="gap"></div>
      <div>E-Mail: info@tbrberater.eu</div>
      <div>Internet: www.tbrberater.eu</div>
    </div>
  </article>
  <article class="card card--back">
    <div class="wordmark wordmark--white">
      <span class="wordmark__name">TBR</span>
      <span class="wordmark__line">STEUERBERATUNG</span>
    </div>
  </article>
</section>

<section class="letter-section">
  <article class="letterhead">
    <div class="wordmark">
      <span class="wordmark__name">TBR</span>
      <span class="wordmark__line">STEUERBERATUNG</span>
    </div>
    <p class="letterhead__sender">TBR Steuerberatung . Lindenweg 17 . 72614 Grünhain</p>
    <span class="fold-mark fold-mark--upper"></span>
    <span class="fold-mark fold-mark--lower"></span>
    <footer class="letterhead__footer">
      <div>
        <div class="accent">Jonas Feldmann</div>
        <div>Steuerberater</div>
        <div>Wirtschaftsprüfer</div>
      </div>
      <div>
        <div class="accent">Lukas Brandner</div>
        <div>Steuerberater</div>
        <div class="accent">Tobias Wendler</div>
        <div>Finanz- und Anlageberater</div>
      </div>
      <div>
        <div>Lindenweg 17</div>
        <div>72614 Grünhain</div>
        <div>E-Mail: info@tbrberatung.eu</div>
        <div>Internet: www.tbrberatung.eu</div>
      </div>
      <div>
        <div class="accent">Bankverbindung</div>
        <div>Kreisbank Grünhain</div>
        <div>BIC: GENODEF1KGH</div>
        <div>IBAN: DE27 6405 0120 0031 4477 82</div>
      </div>
    </footer>
  </article>
</section>

</body>
</html>
```